a modern outdoor type website for our Kestrel Mini Skimcraft for Hunters and Fisherman

look at our current website. www.kestrelskimcraft.example

I want a modern and more progressive design. You are free to go to the website and copy images that are needed. I will want a fully completed website with 5 to 8 pages in wordpress.

Our customers are hunters, fisherman and explorers that want a low cost, high quality product that uses less fuel, is quieter and easy to maintain.

We want to feature our models, our videos and our photos. Customers will want more information about the models, pricing, features, specifications and options. A table can be used on each model for these items, a slide show for the photos and thumbnails of videos which are on our current website.

Colors should include bright but outdoor shades of fall green, brown and tan.

I want a menu bar with submenus like this - Pages/Menu includes Home; Models ( K27M, Vantro, Harbison and Wren 55.); Support (Manuals, Tips, Dealers); Media (photos, videos); Contact;

Two logos are provided for your convenience. use both if possible.

I would like to have a contact page with google map. Our address is 4123 North, 2870 East, West Jordan, Utah 84092

_don't read any further, they require 300 words which are not needed. _

_____________

I want a modern and more progressive design. You are free to go to the website and copy images that are needed.

---------------look at our current website. www.kestrelskimcraft.example

---------------

---------------
Updates

Target Market(s)

outdoor sportsman, hunters, fisherman, explorers on a budget

Industry/Entity Type

Marine

Coding

Coded - Design and coding required

Number of Pages Required

5+ page

Font styles to use
Sans Serif

Colors
fee18a
fce8d3
cadf82

Requirements
Must have
• see the menu items required with corresponding pages.
• Home
• Models
• Support
• Media
• Contact
• and, we need our logo on each page
Nice to have
• when you visit our website www.kestrelskimcraft.example you will see a specs page with different models. I want the menu bar to reflect those models and a page for each showing (features, specifications, options, video and photo slideshow.)
• The front page should show the airboat coming on to the page.
• I work with Dreamweaver and would like the final format so that I can keep it updated with my Dreamweaver software.
Should not have
• I don't want too many bright colors. It should be for guys and for guys that love the outdoors.

```html
<!DOCTYPE html>
<html lang="en">
<head>
<meta charset="utf-8">
<title>Kestrel Mini Skimcraft</title>
<link rel="stylesheet" href="https://fonts.googleapis.com/css2?family=Arimo:wght@400;700&family=Open+Sans:wght@400;600;700&display=swap">
<style>
:root{
  --green:#b7cf6a;
  --green-light:#cadf82;
  --green-dark:#8fab3f;
  --gold:#f3c76a;
  --gold-light:#fee18a;
  --orange-text:#e9b25a;
  --tan:#fce8d3;
  --ink:#2b2b2b;
  --body:#666;
  --grey-band:#ecebe6;
  --footer:#1e1e1e;
  --white:#fff;
}
*{box-sizing:border-box;margin:0;padding:0}
html,body{width:1200px;height:2647px;overflow:hidden}
body{font-family:"Open Sans",Arial,sans-serif;color:var(--body);background:var(--white);position:relative}
h1,h2,h3,h4{font-family:Arimo,Arial,sans-serif;color:var(--ink)}
.wrap{width:1002px;margin:0 auto;position:relative}

/* header */
.site-header{height:95px;border-top:4px solid var(--gold-light);position:relative;background:var(--white)}
.brand{position:absolute;left:85px;top:22px;display:flex;align-items:center;gap:10px}
.brand-dot{width:34px;height:34px;border-radius:50%;background:#c0392b}
.brand-name{font-family:Arimo,Arial,sans-serif;font-weight:700;font-size:30px;color:#c0392b;letter-spacing:1px}
.top-contact{position:absolute;right:98px;top:14px;display:flex;align-items:center;gap:20px;font-size:15px;color:var(--ink)}
.socials{display:flex;gap:6px}
.socials span{width:28px;height:28px;border-radius:50%;display:block}
.s1{background:#3b5998}.s2{background:#1da1f2}.s3{background:#cb2027}
.contact-item{display:flex;align-items:center;gap:8px}
.ring{width:28px;height:28px;border:2px solid var(--green);border-radius:50%;display:flex;align-items:center;justify-content:center}
.main-nav{position:absolute;right:104px;top:62px;display:flex;gap:28px;font-family:Arimo,Arial,sans-serif;font-weight:700;font-size:14px;color:var(--ink)}
.main-nav .active{color:var(--green)}

/* hero */
.hero{height:440px;position:relative;background:linear-gradient(180deg,#4d6a3a 0%,#6f7f55 40%,#8b8670 60%,#5d6e40 100%);text-align:center;overflow:hidden}
.hero-photo{position:absolute;inset:0}
.hero-text{position:relative;padding-top:134px}
.hero-kicker{font-family:Arimo,Arial,sans-serif;font-weight:700;font-size:33px;color:var(--white);text-shadow:0 2px 4px rgba(0,0,0,.5)}
.hero-title{font-family:Arimo,Arial,sans-serif;font-weight:700;font-size:50px;color:var(--white);text-shadow:0 2px 4px rgba(0,0,0,.5);margin-top:2px}
.btn{display:inline-block;font-family:"Open Sans",Arial,sans-serif;font-weight:700;color:var(--white);border-radius:3px;text-transform:uppercase}
.btn-green{background:linear-gradient(180deg,#c5db7a,#9dbb4c);box-shadow:0 2px 0 #86a23a}
.hero .btn{margin-top:24px;padding:16px 28px;font-size:16px}
.slider-dots{position:absolute;left:50%;bottom:40px;transform:translateX(-50%);display:flex;gap:6px}
.slider-dots span{width:32px;height:6px;border-radius:3px;background:var(--white)}
.slider-dots .on{background:var(--green)}

/* values */
.values{height:310px;background:var(--grey-band);text-align:center;padding-top:34px}
.section-title{font-size:25px;font-weight:700;text-transform:uppercase}
.value-list{display:flex;justify-content:space-between;width:1002px;margin:28px auto 0}
.value{width:200px}
.value-icon{width:106px;height:106px;border-radius:50%;background:var(--green);border:4px solid #d9e8a6;margin:0 auto;display:flex;align-items:center;justify-content:center}
.value h3{font-size:16px;margin-top:17px;text-transform:uppercase}
.value p{font-size:13px;line-height:20px;margin-top:6px;color:#777}

/* welcome */
.welcome{height:413px;padding-top:52px}
.welcome-text{width:490px}
.welcome h2{font-size:25px;font-weight:700;text-transform:uppercase}
.lead{color:var(--orange-text);font-size:13px;line-height:22px;margin-top:14px}
.welcome p.copy{font-size:13px;line-height:22px;margin-top:14px}
.welcome-actions{display:flex;align-items:center;gap:18px;margin-top:26px}
.welcome-actions .btn{padding:16px 20px;font-size:13px}
.call{display:flex;align-items:center;gap:10px;font-size:14px;text-transform:uppercase;color:#777}
.call strong{color:var(--green);font-size:23px;font-family:Arimo,Arial,sans-serif}
.video{position:absolute;left:536px;top:0;width:466px;height:310px;background:linear-gradient(180deg,#9fb3c6 0%,#c4ccc6 40%,#6c7a4a 65%,#8a7a55 100%);border:5px solid #eee}
.video-bar{position:absolute;left:0;right:0;top:0;height:30px;background:rgba(0,0,0,.55);color:var(--white);font-size:12px;font-weight:600;padding:7px 12px}
.play{position:absolute;left:50%;top:50%;width:56px;height:56px;margin:-28px 0 0 -28px;border-radius:50%;background:rgba(0,0,0,.6);display:flex;align-items:center;justify-content:center}

/* build band */
.build{height:248px;background:var(--green-light);text-align:center;padding-top:46px;color:var(--white)}
.build h2{color:var(--white);font-size:24px;text-transform:uppercase}
.build p{width:780px;margin:12px auto 0;font-size:14px;line-height:22px;color:#f4f8e6}
.btn-gold{background:linear-gradient(180deg,var(--gold-light),var(--gold));box-shadow:0 2px 0 #d8a84c;padding:16px 0;width:212px;font-size:14px;margin-top:28px}

/* models */
.models{height:514px;padding-top:46px;text-align:center}
.cards{display:flex;justify-content:space-between;margin-top:36px;text-align:left}
.card{width:320px}
.card-photo{height:220px;border:4px solid #eee}
.p1{background:linear-gradient(180deg,#4e5a3e,#6b6a4e 60%,#5c5845)}
.p2{background:linear-gradient(180deg,#7f7d74,#9a9584 50%,#6e6a58)}
.p3{background:linear-gradient(180deg,#6f7564,#8b8872 50%,#5e6048)}
.card h3{font-size:16px;margin-top:20px}
.card p{font-size:12.5px;line-height:21px;margin-top:8px;color:#777}
.more{display:block;color:var(--green);font-size:12px;font-weight:600;margin-top:10px}
.arrow{position:absolute;top:180px}
.arrow.l{left:-28px}.arrow.r{right:-28px}

/* map */
.map{height:328px;background:linear-gradient(135deg,#e9e4d8,#ddd6c6 50%,#e6e1d4)}

/* footer */
.site-footer{height:299px;background:var(--footer);color:#ccc;position:relative}
.foot-brand{position:absolute;left:62px;top:72px;display:flex;align-items:center;gap:10px}
.foot-col{position:absolute;top:40px}
.foot-col h4{color:var(--white);font-size:15px;text-transform:uppercase}
.foot-col ul{list-style:none;margin-top:20px;font-size:12.5px;line-height:26px}
.c-info{left:418px}.c-news{left:591px;width:265px}.c-contact{left:912px;width:220px}
.c-news p{font-size:12.5px;line-height:20px;margin-top:20px}
.email-field{height:34px;background:var(--white);margin-top:14px;color:#888;font-size:12px;padding:9px 12px}
.subscribe{display:inline-block;margin-top:10px;border:2px solid var(--white);color:var(--white);font-size:12px;font-weight:700;padding:7px 12px;border-radius:3px}
.c-contact li{display:flex;gap:14px;margin-bottom:12px;line-height:20px}
.copyright{position:absolute;left:99px;bottom:26px;font-size:12px}
.foot-social{position:absolute;right:104px;bottom:20px;display:flex;gap:6px}
.foot-social span{width:26px;height:26px;border:1.5px solid var(--white);border-radius:50%}
</style>
</head>
<body>

<header class="site-header">
  <div class="brand"><span class="brand-dot"></span><span class="brand-name">KESTREL</span></div>
  <div class="top-contact">
    <div class="socials"><span class="s1"></span><span class="s2"></span><span class="s3"></span></div>
    <div class="contact-item"><span class="ring"><svg width="12" height="12" viewBox="0 0 24 24"><path fill="#b7cf6a" d="M6.6 10.8a15 15 0 006.6 6.6l2.2-2.2c.3-.3.7-.4 1-.2 1.1.4 2.3.6 3.6.6.6 0 1 .4 1 1V20c0 .6-.4 1-1 1A17 17 0 013 4c0-.6.4-1 1-1h3.5c.6 0 1 .4 1 1 0 1.3.2 2.5.6 3.6.1.3 0 .7-.2 1z"/></svg></span>801-555-0148</div>
    <div class="contact-item"><span class="ring"><svg width="12" height="10" viewBox="0 0 24 18"><rect x="1" y="1" width="22" height="16" fill="none" stroke="#b7cf6a" stroke-width="2"/><path d="M1 1l11 9 11-9" fill="none" stroke="#b7cf6a" stroke-width="2"/></svg></span>info@kestrelskimcraft.example</div>
  </div>
  <nav class="main-nav">
    <span class="active">HOME</span><span>MODELS</span><span>SUPPORT</span><span>MEDIA</span><span>CONTACT</span>
    <svg width="14" height="14" viewBox="0 0 24 24"><circle cx="10" cy="10" r="7" fill="none" stroke="#2b2b2b" stroke-width="3"/><path d="M15 15l7 7" stroke="#2b2b2b" stroke-width="3"/></svg>
  </nav>
</header>

<section class="hero">
  <div class="hero-photo" role="img" aria-label="Mini skimcraft with cage propeller moored at a wooden dock among lily pads"></div>
  <div class="hero-text">
    <div class="hero-kicker">Powerful and Lightweight Kestrel Skimcraft Dubbed</div>
    <h1 class="hero-title">"SPORTSMAN'S DREAM"</h1>
    <a class="btn btn-green">View our skimcraft models</a>
  </div>
  <div class="slider-dots"><span class="on"></span><span></span><span></span><span></span></div>
</section>

<section class="values">
  <h2 class="section-title">Value We Offer</h2>
  <div class="value-list">
    <div class="value">
      <div class="value-icon"><svg width="50" height="34" viewBox="0 0 50 34"><rect x="2" y="2" width="46" height="30" rx="3" fill="none" stroke="#fff" stroke-width="3"/><circle cx="25" cy="17" r="8" fill="#fff"/></svg></div>
      <h3>Low Cost</h3><p>Here's the best part, we have the Kestrel priced it to sell</p>
    </div>
    <div class="value">
      <div class="value-icon"><svg width="44" height="44" viewBox="0 0 44 44"><rect x="4" y="20" width="8" height="20" fill="#fff"/><path d="M15 20l8-14c3 0 4 2 3 6l-1 6h11c3 0 4 3 3 5l-4 14c-1 2-2 3-4 3H15z" fill="#fff"/></svg></div>
      <h3>High Quality</h3><p>Here's the best part, we have the Kestrel priced it to sell</p>
    </div>
    <div class="value">
      <div class="value-icon"><svg width="40" height="48" viewBox="0 0 40 48"><rect x="4" y="4" width="22" height="40" rx="2" fill="#fff"/><rect x="8" y="9" width="14" height="10" fill="#b7cf6a"/><path d="M26 14l7 6v18a3 3 0 01-6 0v-8h-1" fill="none" stroke="#fff" stroke-width="3"/></svg></div>
      <h3>Less Fuel Consumption</h3><p>Here's the best part, we have the Kestrel priced it to sell</p>
    </div>
    <div class="value">
      <div class="value-icon"><svg width="50" height="46" viewBox="0 0 50 46"><circle cx="18" cy="26" r="11" fill="none" stroke="#fff" stroke-width="6" stroke-dasharray="5 3"/><circle cx="18" cy="26" r="4" fill="#fff"/><circle cx="38" cy="12" r="7" fill="none" stroke="#fff" stroke-width="4" stroke-dasharray="4 2"/></svg></div>
      <h3>Easy to Maintain</h3><p>Here's the best part, we have the Kestrel priced it to sell</p>
    </div>
  </div>
</section>

<section class="welcome">
  <div class="wrap">
    <div class="welcome-text">
      <h2>Welcome to Kestrel Skimcraft</h2>
      <p class="lead">Discover the shocking new secret of the hunting elite guaranteed to get you into the toughest "hot-spots" with ease... and carry you out with the trophy!</p>
      <p class="copy">It's really quite simple...We build the best mini ultralight skimcraft. Not only light, they are extremely tough. We still build the mini 40 horse Wren which is basically the original Voltrex. It is a tough little motor.But most of our customers want more power and go with the 1300 CC Marrow EFI a good all around boat.</p>
      <p class="copy">But our most serious customers put the Harbison 320 and 360 fresh aircraft motors on our mini Kestrel boats and never look back.</p>
      <div class="welcome-actions">
        <a class="btn btn-green">Read more &gt;&gt;</a>
        <div class="call"><svg width="18" height="18" viewBox="0 0 24 24"><path fill="#888" d="M6.6 10.8a15 15 0 006.6 6.6l2.2-2.2c.3-.3.7-.4 1-.2 1.1.4 2.3.6 3.6.6.6 0 1 .4 1 1V20c0 .6-.4 1-1 1A17 17 0 013 4c0-.6.4-1 1-1h3.5c.6 0 1 .4 1 1 0 1.3.2 2.5.6 3.6.1.3 0 .7-.2 1z"/></svg>Call Dale at <strong>801.555.0148</strong></div>
      </div>
    </div>
    <div class="video" role="img" aria-label="Video still of two riders on a mini skimcraft crossing a marsh under a cloudy sky">
      <div class="video-bar">WE JUST LOVE TO RIDE..</div>
      <div class="play"><svg width="18" height="20" viewBox="0 0 18 20"><path d="M2 1l15 9-15 9z" fill="#fff"/></svg></div>
    </div>
  </div>
</section>

<section class="build">
  <h2>Build your own mini skimcraft with the Kestrel</h2>
  <p>Kestrel 4400 Engine and Belt Drive But our most serious customers put the Harbison 320 and 360 fresh aircraft motors on our mini Kestrel boats and never look back</p>
  <a class="btn btn-gold">Click here to build</a>
</section>

<section class="models">
  <div class="wrap">
    <h2 class="section-title">The Original Kestrel Mini</h2>
    <svg class="arrow l" width="14" height="24" viewBox="0 0 14 24"><path d="M12 2L2 12l10 10" fill="none" stroke="#bbb" stroke-width="2"/></svg>
    <svg class="arrow r" width="14" height="24" viewBox="0 0 14 24"><path d="M2 2l10 10L2 22" fill="none" stroke="#bbb" stroke-width="2"/></svg>
    <div class="cards">
      <article class="card">
        <div class="card-photo p1" role="img" aria-label="Camouflaged mini skimcraft on a trailer under trees"></div>
        <h3>The Kestrel is super easy to trailer</h3>
        <p>One of the biggest issues that most sportsman face is trying to trailer longer boats behind their vehicles. You won't have that issue with the Kestrel.</p>
        <span class="more">READ MORE &gt;&gt;</span>
      </article>
      <article class="card">
        <div class="card-photo p2" role="img" aria-label="Skimcraft loaded with duck decoys in a reedy marsh"></div>
        <h3>Simply dynamite for duck hunting!</h3>
        <p>The Kestrel is the perfect all-around hunting tool. This boat glides on water. Idles quietly. And drives on land with ease! It's suited for all types..</p>
        <span class="more">READ MORE &gt;&gt;</span>
      </article>
      <article class="card">
        <div class="card-photo p3" role="img" aria-label="Camo package skimcraft hidden among marsh grass"></div>
        <h3>The Kestrel camo package</h3>
        <p>We have specially designed our Kestrel skimcraft for the sportsman. Whether duck or dear, you'll blend in. It works great for fishing too!</p>
        <span class="more">READ MORE &gt;&gt;</span>
      </article>
    </div>
  </div>
</section>

<section class="map" role="img" aria-label="Street map showing the shop location at 4123 N 2870 E, West Jordan"></section>

<footer class="site-footer">
  <div class="foot-brand"><span class="brand-dot"></span><span class="brand-name">KESTREL</span></div>
  <div class="foot-col c-info">
    <h4>Information</h4>
    <ul><li>Home</li><li>Models</li><li>Support</li><li>Media</li><li>Contact</li></ul>
  </div>
  <div class="foot-col c-news">
    <h4>Newsletter</h4>
    <p>Register your email address to get information ablout us</p>
    <div class="email-field">Email Address</div>
    <span class="subscribe">SUBSCRIBE</span>
  </div>
  <div class="foot-col c-contact">
    <h4>Contact Us</h4>
    <ul>
      <li><svg width="10" height="14" viewBox="0 0 10 14"><path d="M5 0a5 5 0 015 5c0 4-5 9-5 9S0 9 0 5a5 5 0 015-5z" fill="#ccc"/></svg><span>4123 North, 2870 East,<br>West Jordan, Utah 84092</span></li>
      <li><svg width="12" height="12" viewBox="0 0 24 24"><path fill="#ccc" d="M6.6 10.8a15 15 0 006.6 6.6l2.2-2.2c.3-.3.7-.4 1-.2 1.1.4 2.3.6 3.6.6.6 0 1 .4 1 1V20c0 .6-.4 1-1 1A17 17 0 013 4c0-.6.4-1 1-1h3.5c.6 0 1 .4 1 1 0 1.3.2 2.5.6 3.6.1.3 0 .7-.2 1z"/></svg><span>801-555-0148</span></li>
      <li><svg width="13" height="10" viewBox="0 0 24 18"><rect x="0" y="0" width="24" height="18" fill="#ccc"/><path d="M0 0l12 9 12-9" fill="none" stroke="#1e1e1e" stroke-width="2"/></svg><span>info@kestrelskimcraft.example</span></li>
    </ul>
  </div>
  <div class="copyright">Copyrights © 2016, Kestrel Skimcraft. All rights reserved.</div>
  <div class="foot-social"><span></span><span></span><span></span><span></span></div>
</footer>

</body>
</html>
```